Tour operator needs simple coded WordPress site (updated extra payment for coding and guaranteed)

[update 9/7/2015]
If you design a new logo and it gets accepted, even if we use another template with your logo you will get $50
[update 8/7/2015]
Update on questions about dual-language
For dual languages we are happy to set up a second site with the same designs in a second language.
For the design aspect just allow the user to switch between languages with an icon.
For the coding, a replica of the site on a second server will do (to save messing around with multiple language plugins) - we will populate it with Chinese text
[original post]
Simple coded WordPress site for tours
You can choose to design only or design and code ($340 design, $150 bonus for coding)
Open design brief - use your creativity
Will be in 2 languages (English and Chinese) but design needs only to be in one language
Winning design will be chosen only from home page, but the winner must make a second standard template page when chosen at no extra cost.
Must be responsive design
We only need homepage and standard template page design and coding, we will populate the pages
You can use design ideas from our pamphlet if you like - attached
Only a sample logo and colors on website and pamphlet - feel free to change as the current ones seem restrictive
Current website framework only to give an idea of the number of pages and basic menu structure (no need to use existing navigation style or any style at all for that matter, open brief)
http://brightwattlejourneys.com.au/
Target Market(s)
Chinese parents of kids 10-14 (the kids will take the tour)
Industry/Entity Type
Tour
Number of Pages Required
2 page
Look and feel
Each slider illustrates characteristics of the customer's brand and the style your logo design should communicate.

```html
<!DOCTYPE html>
<html lang="en">
<head>
<meta charset="utf-8">
<title>Bright Wattle Journeys – Cultural Tours of Australia</title>
<link href="https://fonts.googleapis.com/css2?family=Open+Sans:wght@400;600;700&display=swap" rel="stylesheet">
<style>
:root{
  --navy:#1c3b74;
  --blue:#2a58a6;
  --blue-deep:#163064;
  --yellow:#f6b21a;
  --orange:#e8821e;
  --ink:#333b47;
  --muted:#7b838f;
  --line:#e3e6ea;
  --paper:#ffffff;
  --mist:#f3f5f7;
}
*{box-sizing:border-box;margin:0;padding:0}
html,body{width:1200px;height:3020px;overflow:hidden}
body{font-family:"Open Sans",Arial,sans-serif;color:var(--ink);background:var(--paper);font-size:13px;line-height:1.55}
.wrap{width:1024px;margin:0 auto;position:relative}
.btn{display:inline-block;background:var(--yellow);color:#fff;font-weight:700;font-size:11px;text-transform:uppercase;text-align:center;border-radius:2px;padding:9px 0}

/* top bar */
.topbar{height:28px;border-bottom:1px solid var(--line);font-size:10px;color:var(--muted)}
.topbar .wrap{display:flex;justify-content:space-between;align-items:center;height:28px}
.topbar span{margin-right:18px}

/* header */
.header{height:68px}
.header .wrap{display:flex;justify-content:space-between;align-items:center;height:68px}
.brand{display:flex;align-items:center;gap:10px;font-weight:700;font-size:22px;color:var(--orange)}
.brand i{width:14px;height:14px;background:var(--orange);display:block}
.nav{display:flex;gap:30px;font-size:10px;font-weight:600;text-transform:uppercase;color:var(--muted)}
.nav .active{color:var(--navy)}

/* hero */
.hero{height:704px;position:relative;background:linear-gradient(160deg,#6a5a3c 0%,#8a6e45 30%,#4d4a33 60%,#2e3426 100%)}
.hero .wrap{padding-top:270px}
.hero h1{color:#fff;font-size:32px;font-weight:700;line-height:1.28;width:900px}
.booking{margin-top:48px;background:#fff;width:1024px;padding:14px 20px 20px;box-shadow:0 4px 14px rgba(0,0,0,.25);position:relative}
.booking .tab{position:absolute;top:-26px;left:0;background:#fff;padding:5px 18px;font-size:10px;font-weight:600;color:var(--navy)}
.booking h3{font-size:14px;color:var(--navy);font-weight:600;margin-bottom:12px}
.booking .fields{display:flex;gap:10px}
.field{flex:1;height:32px;border:1px solid var(--line);font-size:10px;color:var(--muted);padding:8px 10px;display:flex;justify-content:space-between}
.booking .btn{width:150px;padding:0;line-height:32px}

/* itinerary */
.itinerary{height:658px;padding-top:70px;background:var(--paper)}
.section-title{font-size:17px;font-weight:600;color:var(--navy)}
.rule{width:1024px;height:1px;background:var(--line);margin:12px 0 24px}
.cards{display:flex;gap:24px}
.card{width:325px;border:1px solid var(--line);background:#fff}
.card-photo{height:200px}
.card-body{padding:16px 20px 18px}
.card h4{font-size:12px;font-weight:600;color:var(--ink);margin-bottom:14px}
.card ul{list-style:none;font-size:10px;color:var(--muted);line-height:2}
.card li::before{content:"";display:inline-block;width:5px;height:5px;background:var(--yellow);border-radius:50%;margin-right:8px;vertical-align:middle}
.card .date{text-align:center;font-size:9px;color:var(--muted);margin:34px 0 6px}
.card .btn{width:100%}

/* intro band */
.intro{height:380px;background:linear-gradient(180deg,var(--blue) 0%,var(--blue) 70%,#3c6ab8 100%);position:relative;overflow:hidden}
.intro .skyline{position:absolute;left:0;bottom:0;width:1200px;height:120px;background:linear-gradient(180deg,rgba(255,255,255,0),rgba(255,255,255,.14))}
.intro .wrap{display:flex;padding-top:54px}
.intro-text{width:560px;color:#fff}
.intro-text h2{font-size:17px;line-height:1.5;font-weight:600}
.intro-text h2 em{font-style:normal;color:var(--yellow)}
.intro-text p{font-size:10px;color:#c9d6ee;margin:22px 0 22px;line-height:1.7}
.intro-text .btn{width:110px}
.polaroids{position:relative;width:440px;margin-left:24px}

/* testimonials */
.clients{height:410px;padding-top:30px}
.clients .wrap{display:flex;gap:40px}
.video{width:500px;height:280px;position:relative;background:linear-gradient(135deg,#4a6d8c,#8aa5b8 55%,#55677a)}
.video .bar{position:absolute;left:0;right:0;bottom:0;height:26px;background:rgba(0,0,0,.75)}
.quote{width:484px;padding-top:10px}
.quote .rule{width:484px}
.quote p{font-size:11px;color:var(--muted);line-height:1.8}
.author{display:flex;align-items:center;gap:12px;margin-top:20px;font-size:11px;color:var(--navy);font-weight:600}
.avatar{width:44px;height:44px;border-radius:50%;background:linear-gradient(135deg,#d9b99a,#7a5a48)}
.dots{display:flex;gap:5px;justify-content:flex-end;margin-top:26px}
.dots b{width:7px;height:7px;border-radius:50%;background:var(--line)}
.dots b.on{background:var(--yellow)}

/* why */
.why{height:470px;background:linear-gradient(180deg,var(--blue-deep) 0%,var(--navy) 55%,#27498a 100%);color:#fff;text-align:center;padding-top:46px}
.why h2{font-size:17px;font-weight:600}
.features{display:flex;gap:24px;margin-top:120px}
.feature{flex:1}
.feature .icon{width:56px;height:56px;border-radius:50%;background:var(--yellow);margin:0 auto 14px;display:flex;align-items:center;justify-content:center}
.feature h4{font-size:12px;font-weight:600;margin-bottom:8px}
.feature p{font-size:10px;color:#c5d2ea;line-height:1.7;padding:0 10px}

/* footer */
.footer{height:260px;padding-top:36px}
.footer .wrap{display:flex;gap:34px}
.col{flex:1}
.col h3{font-size:15px;font-weight:600;color:var(--navy);margin-bottom:16px}
.post{display:flex;gap:10px;margin-bottom:16px}
.post .thumb{width:56px;height:46px;flex:none}
.post h5{font-size:11px;color:var(--navy);font-weight:600}
.post p{font-size:9px;color:var(--muted)}
.gallery{display:grid;grid-template-columns:repeat(3,1fr);gap:5px}
.gallery div{height:46px}
.col p.small{font-size:10px;color:var(--muted);line-height:1.7}
.input{height:28px;border:1px solid var(--line);font-size:9px;color:var(--muted);padding:6px 8px;margin:12px 0 8px}
.col .btn{width:90px;padding:7px 0}
.phone{display:flex;align-items:center;gap:8px;font-size:16px;font-weight:700;color:var(--navy);margin:10px 0 4px}
.mail{font-size:10px;color:var(--blue)}
.socials{display:flex;gap:5px;margin-top:12px}
.socials b{width:22px;height:22px;background:#b9c1cc}
.bottombar{height:40px;background:var(--navy);color:#aebbd6;font-size:9px}
.bottombar .wrap{display:flex;justify-content:space-between;align-items:center;height:40px}
</style>
</head>
<body>

<div class="topbar"><div class="wrap">
  <div><span>1 - 8006 - 4421</span><span>info@brightwattlejourneys.com.au</span></div>
  <div><span>Login</span><span>Register</span></div>
</div></div>

<header class="header"><div class="wrap">
  <div class="brand"><i></i>Bright Wattle</div>
  <nav class="nav"><span class="active">Home</span><span>Events</span><span>Tours</span><span>Gallery</span><span>Blog</span><span>Contact</span></nav>
</div></header>

<section class="hero" role="img" aria-label="Photograph of Aboriginal performers in traditional body paint gathered outdoors">
  <div class="wrap">
    <h1>Find out about the rich and multicultural heritage of Australia as it is reflected in the arts</h1>
    <form class="booking">
      <div class="tab">Tours</div>
      <h3>Book with us and we will take care of the rest</h3>
      <div class="fields">
        <div class="field">Choose your tour<span>▾</span></div>
        <div class="field">From<span>▦</span></div>
        <div class="field">To<span>▦</span></div>
        <div class="field">Number of students<span>▾</span></div>
        <span class="btn">Book Now</span>
      </div>
    </form>
  </div>
</section>

<section class="itinerary"><div class="wrap">
  <h2 class="section-title">Itinerary</h2>
  <div class="rule"></div>
  <div class="cards">
    <article class="card">
      <div class="card-photo" role="img" aria-label="Photo of Parliament House, Canberra at sunset" style="background:linear-gradient(180deg,#3a5f9e,#d99a5c 60%,#5b4a3a)"></div>
      <div class="card-body">
        <h4>Australian Tour - Day 1</h4>
        <ul><li>Lorem ipsum dolor sit amet consectetur</li><li>Tour Sydney Museums</li><li>Tour Parliament House</li></ul>
        <div class="date">▦ 10 MAR 2015</div>
        <span class="btn">Book Now</span>
      </div>
    </article>
    <article class="card">
      <div class="card-photo" role="img" aria-label="Photo of a koala resting in a eucalyptus tree" style="background:linear-gradient(160deg,#7e8a6a,#b7b8ad 50%,#5f6b4b)"></div>
      <div class="card-body">
        <h4>Australian Tour - Day 2</h4>
        <ul><li>Lorem ipsum dolor sit amet adipiscing elit</li><li>Tour Taronga Zoo</li><li>Tour Bondi Beach</li></ul>
        <div class="date">▦ 11 MAR 2015</div>
        <span class="btn">Book Now</span>
      </div>
    </article>
    <article class="card">
      <div class="card-photo" role="img" aria-label="Photo of Sydney Opera House and Harbour Bridge" style="background:linear-gradient(180deg,#5d8fc9,#9cc0e2 55%,#3f5f7e)"></div>
      <div class="card-body">
        <h4>Australian Tour - Day 3</h4>
        <ul><li>Lorem ipsum dolor sit amet sed tempor</li><li>Tour Sydney Opera House</li><li>Tour Harbour Bridge</li></ul>
        <div class="date">▦ 12 MAR 2015</div>
        <span class="btn">Book Now</span>
      </div>
    </article>
  </div>
</div></section>

<section class="intro">
  <div class="skyline" role="img" aria-label="Faint city skyline silhouette"></div>
  <div class="wrap">
    <div class="intro-text">
      <h2><em>14 day premium</em> cultural and educational tours to Australian cities. Educational, safe, culturally enlightening and fun. Learn about educational institutions, history, sports, laws and customs, food and culture while improving your English.</h2>
      <p>Lorem ipsum dolor sit amet, consectetur adipiscing elit, sed do eiusmod tempor incididunt ut labore et dolore magna aliqua. Ut enim ad minim veniam, quis nostrud exercitation ullamco laboris nisi ut aliquip ex ea commodo consequat. Duis aute irure dolor in reprehenderit in voluptate velit esse.</p>
      <span class="btn">Learn More</span>
    </div>
    <div class="polaroids">
      <svg width="440" height="270" viewBox="0 0 440 270" role="img" aria-label="Stack of snapshots of smiling students on tour">
        <defs>
          <linearGradient id="ph1" x1="0" y1="0" x2="1" y2="1"><stop offset="0" stop-color="#8fb7d9"/><stop offset="1" stop-color="#d8b58e"/></linearGradient>
          <linearGradient id="ph2" x1="0" y1="0" x2="1" y2="1"><stop offset="0" stop-color="#e3c19a"/><stop offset="1" stop-color="#7d9ec2"/></linearGradient>
        </defs>
        <g transform="rotate(-8 110 140)"><rect x="30" y="40" width="160" height="190" fill="#fff"/><rect x="40" y="50" width="140" height="140" fill="url(#ph1)"/></g>
        <g transform="rotate(6 330 140)"><rect x="250" y="40" width="160" height="190" fill="#fff"/><rect x="260" y="50" width="140" height="140" fill="url(#ph2)"/></g>
        <g transform="rotate(-2 220 130)"><rect x="130" y="20" width="180" height="215" fill="#fff"/><rect x="141" y="31" width="158" height="160" fill="url(#ph2)"/></g>
      </svg>
    </div>
  </div>
</section>

<section class="clients"><div class="wrap">
  <div class="video" role="img" aria-label="Video still of students visiting a landmark">
    <svg width="500" height="280" viewBox="0 0 500 280">
      <circle cx="250" cy="128" r="30" fill="#d8322e"/>
      <path d="M240 113 L265 128 L240 143 Z" fill="#fff"/>
    </svg>
    <div class="bar"></div>
  </div>
  <div class="quote">
    <h2 class="section-title">What Our Clients Say</h2>
    <div class="rule"></div>
    <p>Lorem ipsum dolor sit amet, consectetuer adipiscing elit, sed diam nonummy nibh euismod tincidunt ut laoreet dolore magna aliquam erat volutpat. Ut wisi enim ad minim veniam, quis nostrud exerci tation ullamcorper suscipit lobortis nisl ut aliquip ex ea commodo consequat.</p>
    <div class="author"><div class="avatar" role="img" aria-label="Portrait of the parent"></div>Ms Huang's</div>
    <div class="dots"><b class="on"></b><b></b><b></b></div>
  </div>
</div></section>

<section class="why"><div class="wrap">
  <h2>Why Bright Wattle Journeys?</h2>
  <div class="features">
    <div class="feature">
      <div class="icon"><svg width="26" height="26" viewBox="0 0 26 26"><path d="M3 12 L13 4 L23 12 V23 H3 Z" fill="none" stroke="#fff" stroke-width="2"/><rect x="10" y="15" width="6" height="8" fill="#fff"/></svg></div>
      <h4>Accommodation</h4>
      <p>Comfortable accommodation with carefully selected host families, close to every venue.</p>
    </div>
    <div class="feature">
      <div class="icon"><svg width="26" height="26" viewBox="0 0 26 26"><path d="M3 6 H23 V19 H3 Z" fill="none" stroke="#fff" stroke-width="2"/><path d="M9 23 H17" stroke="#fff" stroke-width="2"/></svg></div>
      <h4>Excursions and Lectures</h4>
      <p>Guided visits and lively lectures help students learn and practise their English daily.</p>
    </div>
    <div class="feature">
      <div class="icon"><svg width="26" height="26" viewBox="0 0 26 26"><circle cx="13" cy="13" r="9" fill="none" stroke="#fff" stroke-width="2"/><path d="M4 13 H22 M13 4 V22" stroke="#fff" stroke-width="2"/></svg></div>
      <h4>Outdoor Activities and Sports</h4>
      <p>Beach days, team sports and nature walks keep the group active and having fun.</p>
    </div>
    <div class="feature">
      <div class="icon"><svg width="26" height="26" viewBox="0 0 26 26"><rect x="4" y="7" width="18" height="11" rx="2" fill="none" stroke="#fff" stroke-width="2"/><circle cx="8" cy="20" r="2" fill="#fff"/><circle cx="18" cy="20" r="2" fill="#fff"/></svg></div>
      <h4>Guides and Transportation</h4>
      <p>Friendly bilingual guides and safe private coaches accompany students at all times.</p>
    </div>
  </div>
</div></section>

<footer class="footer"><div class="wrap">
  <div class="col">
    <h3>Latest Posts</h3>
    <div class="post"><div class="thumb" role="img" aria-label="Thumbnail of a city harbour" style="background:linear-gradient(135deg,#d39a55,#5a7ba8)"></div><div><h5>Lorem Ipsum Dolor</h5><p>Sed ut perspiciatis unde omnis iste natus error sit</p></div></div>
    <div class="post"><div class="thumb" role="img" aria-label="Thumbnail of students on an excursion" style="background:linear-gradient(135deg,#7aa2c8,#c9b08a)"></div><div><h5>Duis Autem Vel Eum</h5><p>Nemo enim ipsam voluptatem quia voluptas sit</p></div></div>
  </div>
  <div class="col">
    <h3>Gallery</h3>
    <div class="gallery" role="img" aria-label="Grid of tour photos">
      <div style="background:#c59a63"></div><div style="background:#6d8fb8"></div><div style="background:#8a6f52"></div>
      <div style="background:#7fa0c2"></div><div style="background:#b58e68"></div><div style="background:#5c7a5a"></div>
      <div style="background:#a7b9cc"></div><div style="background:#d1a570"></div><div style="background:#4f6f98"></div>
    </div>
  </div>
  <div class="col">
    <h3>Mailing List</h3>
    <p class="small">Sign up for our mailing list to get latest updates and offers.</p>
    <div class="input">Your email address</div>
    <span class="btn">Subscribe</span>
    <p class="small" style="margin-top:8px">We respect your privacy</p>
  </div>
  <div class="col">
    <h3>Get In Touch</h3>
    <p class="small">We listen and then help you discover Australia's cultural richness for your family.</p>
    <div class="phone"><svg width="16" height="16" viewBox="0 0 16 16"><path d="M3 1 L6 1 L7 5 L5 6 Q6 9 10 11 L11 9 L15 10 L15 13 Q14 15 12 15 Q2 13 1 3 Q1 1 3 1 Z" fill="var(--navy)"/></svg>1 - 8006 - 4421</div>
    <div class="mail">info@brightwattlejourneys.com.au</div>
    <div class="socials"><b></b><b></b><b></b><b></b><b></b><b></b></div>
  </div>
</div></footer>

<div class="bottombar"><div class="wrap">
  <span>Copyright © Bright Wattle Journeys. All rights reserved.</span>
  <span>▲</span>
</div></div>

</body>
</html>
```